Trvmlegal.com needs a wedsite. Law Office of Darnell P. Whitby

Darnell P. Whitby is a criminal law firm that is 5 years old. We have already had all the content written and now just need the website designed. We also just finished our logo design using Pixel Harbor and would like it used in the design of the website.

Industry/Entity Type

Law Firm

Number of Pages Required

5+ page

Requirements
Must have
• I was our new logo to be on the website also. I want Dallas sites as the stock pictures for the website. For example the Grey Stone Tribunal. I also need to be able to add YouTube videos. It has to adjust to be seen on computers and also cell phones. I need to be able to have a information sheet for clients to fill out and submit back to me.

```html
<!DOCTYPE html>
<html lang="en">
<head>
<meta charset="utf-8">
<title>Law Office of Darnell P. Whitby</title>
<link href="https://fonts.googleapis.com/css2?family=Open+Sans:wght@400;600;700&family=PT+Serif:wght@400;700&display=swap" rel="stylesheet">
<style>
  :root {
    --navy: #0f2757;
    --navy-deep: #0a1c40;
    --button: #15346f;
    --ink: #2b2f38;
    --muted: #6a6f7a;
    --rule: #c9ced8;
    --white: #ffffff;
    --hero-a: #1d2431;
    --hero-b: #5d6675;
    --band-a: #2a2724;
    --band-b: #6b5d52;
  }
  * { box-sizing: border-box; margin: 0; padding: 0; }
  html, body { width: 791px; height: 1200px; overflow: hidden; }
  body { font-family: "Open Sans", Arial, sans-serif; color: var(--ink); background: var(--white); position: relative; }

  .btn {
    display: inline-block; background: var(--button); color: var(--white);
    font-family: "Open Sans", Arial, sans-serif; font-size: 13px; font-weight: 600;
    padding: 8px 26px; border-radius: 2px; text-decoration: none;
  }

  /* Hero */
  .hero { position: absolute; top: 0; left: 0; width: 791px; height: 382px; }
  .hero-photo {
    position: absolute; inset: 0;
    background: linear-gradient(180deg, var(--hero-a) 0%, var(--hero-b) 45%, var(--hero-a) 100%);
  }
  .hero-shade { position: absolute; inset: 0; background: linear-gradient(180deg, rgba(5,10,25,.35), rgba(5,10,25,.15) 40%, rgba(5,10,25,.55)); }

  .brand { position: absolute; left: 28px; top: 14px; display: flex; align-items: center; gap: 8px; }
  .brand-dot { width: 14px; height: 14px; border-radius: 50%; background: var(--white); }
  .brand-name { font-family: "PT Serif", Georgia, serif; font-size: 15px; font-weight: 700; color: var(--white); width: 170px; line-height: 1.2; }

  .call { position: absolute; right: 30px; top: 12px; color: var(--white); font-size: 13px; display: flex; align-items: center; gap: 6px; }
  .call strong { font-size: 15px; font-weight: 700; }
  .call svg { width: 14px; height: 14px; }

  .nav { position: absolute; right: 30px; top: 40px; display: flex; }
  .nav a { color: var(--white); font-size: 11px; font-weight: 600; text-decoration: none; padding: 0 10px; border-left: 1px solid rgba(255,255,255,.4); white-space: nowrap; }
  .nav a:first-child { border-left: none; border-bottom: 2px solid var(--white); padding-bottom: 3px; }
  .nav-sub { position: absolute; left: 255px; top: 68px; background: var(--button); color: var(--white); font-size: 11px; font-weight: 600; padding: 6px 14px; }

  .hero-copy { position: absolute; top: 172px; left: 0; width: 791px; text-align: center; color: var(--white); }
  .hero-copy h1 { font-family: "PT Serif", Georgia, serif; font-size: 29px; font-weight: 400; line-height: 1.2; }
  .hero-copy p { font-size: 15px; font-weight: 600; line-height: 1.35; margin: 8px auto 16px; width: 470px; }
  .hero-dots { position: absolute; top: 348px; left: 0; width: 791px; display: flex; justify-content: center; gap: 6px; }
  .hero-dots span { width: 8px; height: 8px; border-radius: 50%; background: rgba(255,255,255,.5); }
  .hero-dots span:first-child { background: var(--white); }

  /* Welcome */
  .welcome { position: absolute; top: 382px; left: 0; width: 791px; height: 218px; text-align: center; }
  .section-title { display: flex; align-items: center; justify-content: center; gap: 16px; font-family: "PT Serif", Georgia, serif; font-size: 17px; font-weight: 400; color: var(--navy); white-space: nowrap; }
  .section-title::before, .section-title::after { content: ""; height: 1px; width: 150px; background: var(--rule); }
  .welcome .section-title { margin-top: 42px; }
  .welcome p { width: 620px; margin: 16px auto 20px; font-size: 10.5px; line-height: 1.55; color: var(--muted); }

  /* Call to action band */
  .band { position: absolute; top: 600px; left: 0; width: 791px; height: 230px; }
  .band-photo { position: absolute; inset: 0; background: linear-gradient(90deg, var(--band-a), var(--band-b) 50%, var(--band-a)); }
  .band-copy { position: absolute; inset: 0; text-align: center; color: var(--white); padding-top: 66px; }
  .band-copy h2 { font-family: "PT Serif", Georgia, serif; font-size: 23px; font-weight: 400; line-height: 1.4; }
  .band-copy .btn { margin-top: 26px; }

  /* Videos */
  .videos { position: absolute; top: 830px; left: 0; width: 791px; height: 290px; }
  .videos .section-title { margin-top: 20px; font-size: 18px; }
  .videos .section-title::before, .videos .section-title::after { width: 240px; }
  .video-text { position: absolute; left: 116px; top: 58px; width: 270px; }
  .video-text h3 { font-size: 11px; font-weight: 700; color: var(--navy); margin-bottom: 8px; line-height: 1.4; }
  .video-text p { font-size: 9.5px; line-height: 1.55; color: var(--muted); margin-bottom: 8px; }
  .checks { list-style: none; }
  .checks li { display: flex; align-items: center; gap: 6px; font-size: 9.5px; color: var(--muted); margin-bottom: 5px; }
  .checks svg { width: 11px; height: 11px; flex: none; }
  .video-text .btn { margin-top: 12px; }
  .video-frame { position: absolute; left: 403px; top: 66px; width: 288px; height: 186px; background: #111; padding: 0 0 16px; }
  .video-still { width: 100%; height: 100%; background: linear-gradient(135deg, #8a98a8, #3b4656 55%, #1e2530); }
  .video-bar { position: absolute; left: 0; bottom: 0; width: 100%; height: 16px; background: #1b1b1b; }
  .video-bar::after { content: ""; position: absolute; left: 30px; right: 50px; top: 7px; height: 2px; background: #555; }

  /* Footer */
  .footer { position: absolute; top: 1120px; left: 0; width: 791px; height: 80px; background: var(--navy); color: var(--white); }
  .footer-links { position: absolute; left: 116px; top: 22px; font-size: 10px; font-weight: 600; }
  .footer-links span { padding: 0 6px; opacity: .6; }
  .copyright { position: absolute; left: 116px; top: 40px; font-size: 9px; opacity: .85; }
  .social { position: absolute; right: 100px; top: 20px; display: flex; gap: 4px; }
  .social span { width: 18px; height: 18px; background: #2d5fa8; }
</style>
</head>
<body>

<header class="hero">
  <div class="hero-photo" role="img" aria-label="Photograph of tall stone courthouse columns in dark blue tones"></div>
  <div class="hero-shade"></div>

  <div class="brand">
    <span class="brand-dot"></span>
    <span class="brand-name">Law Office of Darnell P. Whitby</span>
  </div>

  <div class="call">
    Call us
    <svg viewBox="0 0 24 24" fill="#fff" aria-hidden="true"><path d="M6.6 10.8a15 15 0 0 0 6.6 6.6l2.2-2.2a1 1 0 0 1 1-.25 11.4 11.4 0 0 0 3.6.57 1 1 0 0 1 1 1V20a1 1 0 0 1-1 1A17 17 0 0 1 3 4a1 1 0 0 1 1-1h3.5a1 1 0 0 1 1 1c0 1.25.2 2.45.57 3.57a1 1 0 0 1-.25 1z"/></svg>
    <strong>972.555.0148</strong>
  </div>

  <nav class="nav">
    <a href="#">Attorney Profile</a>
    <a href="#">Murder &amp; Other Homicide Offenses</a>
    <a href="#">Expungements &amp; Non-Disclosures</a>
  </nav>
  <div class="nav-sub">How We Can Help</div>

  <div class="hero-copy">
    <h1>Solutions to the most challenging problems</h1>
    <p>Lorem ipsum dolor sit amet consectetur adipiscing elit. Quid sequatur quid repugnet vident.</p>
    <a class="btn" href="#">Read More</a>
  </div>
  <div class="hero-dots"><span></span><span></span><span></span><span></span></div>
</header>

<section class="welcome">
  <h2 class="section-title">Welcome to Law office of Darnell P. Whitby</h2>
  <p>Our firm has defended clients across Dallas County for five years. We handle felony and misdemeanor cases with care, preparation and steady courtroom experience. Every case receives personal attention from the first call through the final ruling, and we explain each step so you always know where you stand.</p>
  <a class="btn" href="#">Read More</a>
</section>

<section class="band">
  <div class="band-photo" role="img" aria-label="Photograph of an attorney meeting with clients in warm brown tones"></div>
  <div class="band-copy">
    <h2>Have a case that needs resolving?<br>Give us the facts and we'll take care of the rest.</h2>
    <a class="btn" href="#">Get In Touch Now</a>
  </div>
</section>

<section class="videos">
  <h2 class="section-title">Featured Videos</h2>
  <div class="video-text">
    <h3>Lorem ipsum dolor sit amet consectetur adipiscing elit.</h3>
    <p>Watch short answers to common questions about arrests, bail hearings, plea offers and clearing your record. New videos are added each month.</p>
    <ul class="checks">
      <li><svg viewBox="0 0 12 12" aria-hidden="true"><circle cx="6" cy="6" r="6" fill="#15346f"/><path d="M3.3 6.2l1.8 1.7 3.6-3.7" stroke="#fff" stroke-width="1.4" fill="none"/></svg>Lorem ipsum dolor sit amet consectetur adipiscing elit</li>
      <li><svg viewBox="0 0 12 12" aria-hidden="true"><circle cx="6" cy="6" r="6" fill="#15346f"/><path d="M3.3 6.2l1.8 1.7 3.6-3.7" stroke="#fff" stroke-width="1.4" fill="none"/></svg>Lorem ipsum dolor sit amet consectetur adipiscing elit</li>
    </ul>
    <a class="btn" href="#">Watch More</a>
  </div>
  <div class="video-frame">
    <div class="video-still" role="img" aria-label="Video still of a group of business people in an office"></div>
    <div class="video-bar"></div>
  </div>
</section>

<footer class="footer">
  <div class="footer-links">Attorney Profile<span>|</span>Murder &amp; Other Homicide Offenses<span>|</span>Expungements &amp; Non-Disclosures</div>
  <div class="copyright">Copyright © 2017 Law Office of Darnell P. Whitby. All rights reserved.</div>
  <div class="social" aria-label="Social links"><span></span><span></span><span></span><span></span></div>
</footer>

</body>
</html>
```